[AMAZING DESIGN NEEDED] Women's Fishing Squeeze Page

I need a professional design for a landing page that is going to collect email addresses.

You can use the creatives already on the page or you can pull images from the facebook/instagram pages.
https://www.facebook.com/LuresLinesLaces
https://www.instagram.com/lureslinesandlaces/

This is the page that needs designed: https://lureslinesandlaces-example.com/email-opt-in/

See attached for examples.

Target Market(s)

Women who like to go fishing

Industry/Entity Type

Fishing

Number of Pages Required

1 page

Font styles to use
Sans Serif

Requirements
Must have
• excellent design. Call to actions.

```html
<!DOCTYPE html>
<html lang="en">
<head>
<meta charset="utf-8">
<title>Lures, Lines &amp; Laces – Sign Up</title>
<link rel="stylesheet" href="https://fonts.googleapis.com/css2?family=Hanken+Grotesk:wght@400;500;600&family=Dancing+Script:wght@600&display=swap">
<style>
:root{
  --sand:#cdbaa9;
  --teal:#007b7b;
  --brown:#4a3628;
  --text:#6e4c38;
  --field:#e6e6e6;
  --white:#ffffff;
}
*{box-sizing:border-box;margin:0;padding:0}
html,body{width:1169px;height:1200px;overflow:hidden}
body{background:var(--sand);font-family:"Hanken Grotesk",sans-serif;color:var(--brown);position:relative}
.abs{position:absolute}
/* header */
.site-header{position:absolute;left:0;top:0;width:1169px;height:117px;background:var(--sand);z-index:2}
.brand-disc{left:90px;top:37px;width:124px;height:124px;border-radius:50%;background:var(--sand);z-index:2}
.brand-name{left:86px;top:42px;width:150px;color:var(--teal);font-weight:600;font-size:20px;line-height:1.05;z-index:3}
.util{top:33px;font-size:14px;font-weight:500;color:var(--brown)}
.icon-btn{top:28px;width:31px;height:31px;border-radius:50%;background:var(--brown);display:flex;align-items:center;justify-content:center;color:var(--white);font-size:11px;font-weight:600}
.cart{left:872px;top:28px;width:125px;height:31px;border-radius:16px;background:var(--teal);color:var(--white);font-size:14px;font-weight:600;display:flex;align-items:center;justify-content:center;gap:7px}
.main-nav{right:88px;top:82px;display:flex;gap:34px;font-size:14px;font-weight:500;letter-spacing:.3px;color:var(--brown)}
/* hero */
.hero{left:0;top:117px;width:1169px;height:693px;background:var(--teal)}
.hero-photo{left:0;top:117px;width:841px;height:693px;background:linear-gradient(160deg,#7e9a46 0%,#a9b85d 35%,#6f8a56 65%,#8f9a74 100%)}
.card{left:600px;top:284px;width:483px;height:437px;background:var(--white);border-radius:10px}
.card-disc{left:763px;top:206px;width:156px;height:156px;border-radius:50%;background:var(--white)}
.card-brand{left:763px;top:252px;width:156px;text-align:center;color:var(--teal);font-weight:600;font-size:16px;line-height:1.1}
.card-title{left:600px;top:346px;width:483px;text-align:center;font-family:"Dancing Script",cursive;font-size:60px;font-weight:600;color:var(--brown);line-height:1}
.card-sub{left:600px;top:425px;width:483px;text-align:center;font-size:22px;color:var(--brown);letter-spacing:.3px}
.card-sub em{color:var(--teal)}
.field{left:631px;width:421px;height:39px;border-radius:20px;background:var(--field);font-size:14px;padding-left:20px;display:flex;align-items:center;color:var(--brown)}
.cta{left:631px;top:641px;width:421px;height:39px;border-radius:20px;background:var(--teal);color:var(--white);font-size:14px;font-weight:600;letter-spacing:.5px;display:flex;align-items:center;justify-content:center}
/* footer */
.foot-h{top:884px;font-size:19px;font-weight:500;color:var(--brown);letter-spacing:.3px}
.foot-list{top:921px;list-style:none;font-size:14px;line-height:23.4px;color:var(--text);letter-spacing:.2px}
.phone{font-weight:600;color:var(--text)}
.news-input{left:771px;top:975px;width:312px;height:39px;border-radius:20px;border:1px solid var(--brown);background:var(--white);font-size:14px;padding-left:16px;display:flex;align-items:center}
.news-btn{left:771px;top:1021px;width:125px;height:39px;border-radius:20px;background:var(--brown);color:var(--white);font-size:14px;font-weight:600;letter-spacing:.5px;display:flex;align-items:center;justify-content:center}
.social{top:1029px;width:31px;height:31px;border-radius:50%;display:flex;align-items:center;justify-content:center;color:var(--white);font-size:11px;font-weight:600}
.copy{left:86px;top:1135px;font-size:14px;color:var(--text)}
.pay{left:530px;top:1136px;display:flex;gap:16px;font-size:12px;font-weight:600;color:var(--text)}
</style>
</head>
<body>
<header class="site-header">
  <span class="abs util" style="left:534px">Gift Certificates</span>
  <span class="abs util" style="left:655px">|</span>
  <span class="abs util" style="left:675px">Sign in or Register</span>
  <span class="abs icon-btn" style="left:825px" aria-label="Search">
    <svg width="13" height="13" viewBox="0 0 13 13"><circle cx="7.5" cy="5.5" r="4" fill="none" stroke="#fff" stroke-width="1.5"/><line x1="4.5" y1="8.5" x2="1" y2="12" stroke="#fff" stroke-width="1.5"/></svg>
  </span>
  <span class="cart abs">
    <svg width="13" height="12" viewBox="0 0 13 12"><path d="M0 1h2l2 7h7l1.5-5H3" fill="none" stroke="#fff" stroke-width="1.3"/><circle cx="5" cy="10.5" r="1" fill="#fff"/><circle cx="10" cy="10.5" r="1" fill="#fff"/></svg>
    Cart $0.00
  </span>
  <span class="abs icon-btn" style="left:1012px" aria-label="Netfold">N</span>
  <span class="abs icon-btn" style="left:1051px" aria-label="Pictoria">P</span>
  <nav class="abs main-nav">
    <span>CLOTHING</span><span>HATS</span><span>BUNDLES</span><span>ACCESSORIES &amp; STICKERS</span><span>JEWELRY</span><span>CLEARANCE</span>
  </nav>
</header>
<div class="abs brand-disc"></div>
<div class="abs brand-name">Lures, Lines<br>&amp; Laces</div>

<section>
  <div class="abs hero"></div>
  <div class="abs hero-photo" role="img" aria-label="Smiling woman fly fishing in a clear river with her black dog, green trees behind"></div>
  <div class="abs card"></div>
  <div class="abs card-disc"></div>
  <div class="abs card-brand">Lures, Lines<br>&amp; Laces</div>
  <h1 class="abs card-title">Sign Up Today</h1>
  <p class="abs card-sub">And receive <em>15% off</em> your next order</p>
  <div class="abs field" style="top:477px">First Name</div>
  <div class="abs field" style="top:532px">Last Name</div>
  <div class="abs field" style="top:587px">Email Address *</div>
  <div class="abs cta">SUBSCRIBE AND SAVE</div>
</section>

<footer>
  <h2 class="abs foot-h" style="left:86px">Navigate</h2>
  <ul class="abs foot-list" style="left:86px"><li>Trips</li><li>Shipping &amp; Returns</li><li>Contact Us</li><li>Blog</li><li>Sitemap</li></ul>
  <h2 class="abs foot-h" style="left:312px">Categories</h2>
  <ul class="abs foot-list" style="left:312px"><li>Clothing</li><li>Hats</li><li>Bundles</li><li>Accessories &amp; Stickers</li><li>Jewelry</li><li>Clearance</li></ul>
  <h2 class="abs foot-h" style="left:530px">Info</h2>
  <ul class="abs foot-list" style="left:530px"><li>Montana</li><li class="phone" style="font-size:15px">Call us at 4065550147</li></ul>
  <h2 class="abs foot-h" style="left:530px;top:984px">Connect With Us</h2>
  <span class="abs social" style="left:530px;background:var(--teal)" aria-label="Netfold">N</span>
  <span class="abs social" style="left:569px;background:var(--brown)" aria-label="Pictoria">P</span>
  <h2 class="abs foot-h" style="left:771px">Subscribe to our newsletter</h2>
  <p class="abs" style="left:771px;top:922px;width:300px;font-size:14px;line-height:1.1;color:var(--text)">Get the latest updates on new products and upcoming sales</p>
  <div class="abs news-input">Your email address...</div>
  <div class="abs news-btn">SUBSCRIBE</div>
  <p class="abs copy">© 2021 Lures, Lines &amp; Laces</p>
  <div class="abs pay"><span>Amerigo Pay</span><span>Discera</span><span>Mastline</span><span>PayPort</span><span>Versa</span></div>
</footer>
</body>
</html>
```